Aviation: Overcast Study Guide Book Cover

We need a book cover (front and back) designed for an Instrument Flight Rules (IFR) study guide used by helicopter and airplane pilots to obtain an instrument rating for a helicopter or airplane. Below is the title and subtitles.

TITLE: OVERCAST STUDY GUIDE
SUBTITLE 1: Checkride Preparation for Airplane and Helicopter Pilots
SUBTITLE 2: Prepare for your Instrument Rating with Confidence

We have also upload recommended text to be included on the back cover. In addition, we included images of similar book covers that we like and ones that we do not like. Below are links to two others books by the author.

https://www.bookvarro.example/Rotorcraft-Exam-Handbook-oral-review/dp/507214638K
https://www.bookvarro.example/Manual-Floatwing-Handling-Lionel-Quarrick/dp/5093742816

Flight students

Aviation

• helicopter and airplane

```html
<!DOCTYPE html>
<html lang="en">
<head>
<meta charset="utf-8">
<title>Overcast Study Guide – Cover Spread</title>
<link rel="stylesheet" href="https://fonts.googleapis.com/css2?family=Montserrat:ital,wght@0,400;0,500;0,600;0,700;0,800;0,900;1,500&display=swap">
<style>
  :root {
    --page-bg: #e3e8ec;
    --cover-top: #0e6b93;
    --cover-mid: #11527d;
    --cover-bottom: #0b1c42;
    --accent: #f0a81e;
    --ink-light: #ffffff;
    --ink-soft: #e4edf3;
    --tag-bg: #1a5a86;
    --gauge-face: #1c1f24;
  }
  * { box-sizing: border-box; margin: 0; padding: 0; }
  html, body { width: 835px; height: 1200px; overflow: hidden; }
  body {
    background: var(--page-bg);
    font-family: "Montserrat", sans-serif;
    position: relative;
  }
  .cover-spread {
    position: absolute;
    left: 20px; top: 313px;
    width: 795px; height: 573px;
    background: linear-gradient(180deg, var(--cover-top) 0%, var(--cover-mid) 55%, var(--cover-bottom) 88%);
    overflow: hidden;
    color: var(--ink-light);
  }

  /* Back cover */
  .back-cover { position: absolute; left: 25px; top: 38px; width: 305px; }
  .back-heading {
    font-size: 8.6px; font-weight: 700; color: var(--accent);
    letter-spacing: -0.1px; margin-bottom: 4px;
  }
  .back-copy {
    font-size: 7.6px; line-height: 9.9px; text-align: justify;
    color: var(--ink-soft); margin-bottom: 8px;
  }
  .topic-grid {
    display: grid; grid-template-columns: repeat(3, 95px);
    column-gap: 8px; row-gap: 5px; margin-top: 24px;
  }
  .topic-tag {
    background: var(--tag-bg); height: 14px;
    font-size: 6.6px; line-height: 14px; padding-left: 6px;
    color: var(--ink-soft);
  }
  .about-title {
    font-size: 16px; font-weight: 400; margin: 16px 0 8px;
  }
  .about-title strong { font-weight: 800; color: var(--accent); }
  .about-copy { font-size: 7.8px; line-height: 11.9px; text-align: justify; color: var(--ink-soft); }
  .about-copy em { font-style: italic; }

  /* Spine */
  .spine {
    position: absolute; left: 386px; top: 34px; width: 28px; height: 520px;
    display: flex; flex-direction: column; align-items: center;
  }
  .spine-text {
    writing-mode: vertical-rl;
    font-weight: 900; white-space: nowrap;
  }
  .spine-title { font-size: 21px; color: var(--ink-light); letter-spacing: 0.5px; }
  .spine-author { font-size: 14px; color: var(--accent); margin-top: 26px; font-weight: 800; }

  /* Front cover */
  .front-cover { position: absolute; left: 426px; top: 0; width: 369px; height: 573px; }
  .front-title { position: absolute; left: 19px; top: 32px; font-weight: 900; }
  .title-accent { display: block; font-size: 42px; line-height: 1; color: var(--accent); letter-spacing: -1.5px; }
  .title-main { display: block; font-size: 62px; line-height: 0.9; color: var(--ink-light); letter-spacing: -1px; }
  .front-subtitle {
    position: absolute; left: 19px; top: 214px; width: 215px;
    border-top: 1px solid var(--accent); border-bottom: 1px solid var(--accent);
    padding: 3px 4px; font-size: 11px; line-height: 14px;
  }
  .front-subtitle .sub-strong { font-weight: 700; }
  .cockpit-photo {
    position: absolute; left: 0; top: 264px; width: 369px; height: 196px;
    background: radial-gradient(ellipse at 50% 45%, #9aa6b2 0%, #5b6b7c 40%, #1d3153 78%, rgba(11,28,66,0) 100%);
  }
  .gauge-column { position: absolute; left: 265px; top: 0; width: 80px; height: 440px; }
  .gauge { position: absolute; left: 0; }
  .front-tagline {
    position: absolute; left: 19px; top: 467px;
    font-size: 12.6px; font-weight: 800; letter-spacing: 1.6px; line-height: 16px;
  }
  .front-tagline .tag-accent { color: var(--accent); }
  .front-rule { position: absolute; left: 19px; top: 502px; width: 312px; height: 1px; background: var(--ink-light); }
  .front-author {
    position: absolute; left: 19px; top: 517px;
    font-size: 19px; font-weight: 900; color: var(--accent); letter-spacing: 0.8px;
  }
</style>
</head>
<body>
  <main class="cover-spread">
    <section class="back-cover">
      <h2 class="back-heading">PREPARE FOR YOUR IFR CHECK RIDE WITH CONFIDENCE</h2>
      <p class="back-copy">Becoming an instrument rated pilot is one of the most challenging ratings to obtain. This guide helps prepare you to pass your IFR check ride with confidence. The question-and-answer format is easy to follow and provides detailed explanations for expanded knowledge.</p>
      <h2 class="back-heading">INCLUDES HELICOPTER AND AIRPLANE SPECIFIC CONTENT</h2>
      <p class="back-copy">This guide is designed to prepare an airplane or helicopter pilot the oral portion of the IFR checkride. Unlike other resources, this guide specifically addresses the differences with IFR flight in helicopters. As a dual rated pilot, the author ensures to identify areas of differences between the two categories of IFR flight. The following concepts are addressed within the guide.</p>
      <div class="topic-grid">
        <span class="topic-tag">Preflight Actions</span>
        <span class="topic-tag">Enroute Procedures</span>
        <span class="topic-tag">Aeromedical Factors</span>
        <span class="topic-tag">General IFR Concepts</span>
        <span class="topic-tag">Approach Procedures</span>
        <span class="topic-tag">Weather Fundamentals</span>
        <span class="topic-tag">Departure Procedures</span>
        <span class="topic-tag">IFR Emergence</span>
        <span class="topic-tag">Risk Management</span>
      </div>
      <h2 class="about-title"><strong>About</strong> the Author</h2>
      <p class="about-copy">Lionel Quarrick is ATP rated pilot and helicopter and fixed-wing instructor. Lionel is the owner and operator Vantage Crest, LLC which does business as Hoverline Aviation and Pike Aviation. Hoverline Aviation provides primary helicopter flight instruction while Pike Aviation provides seaplane flight instruction and tours. In addition to instructing, Lionel has authored other books to include <em>The Rotorcraft Exam Handbook</em>, and <em>Manual of Floatwing Handling</em>. Lionel lives in Kentucky with his beautiful wife Marla. They have a daughter, Jenna, that is dual rated and employed as a captain for a charter company. Prior to learning to fly, Lionel spent several years in the military as a Special Warfare Combat Craft Crewman in the U.S. Navy and Ranger-qualified Infantry Officer in the State Army National Guard.</p>
    </section>

    <aside class="spine">
      <span class="spine-text spine-title">OVERCAST STUDY GUIDE</span>
      <span class="spine-text spine-author">LIONEL J. QUARRICK</span>
    </aside>

    <section class="front-cover">
      <div class="cockpit-photo" role="img" aria-label="Photograph of an aircraft cockpit instrument panel with glass displays and control yokes"></div>
      <h1 class="front-title">
        <span class="title-accent">OVERCAST</span>
        <span class="title-main">STUDY</span>
        <span class="title-main">GUIDE</span>
      </h1>
      <p class="front-subtitle">CHECKRIDE PREPARATION FOR<br><span class="sub-strong">AIRPLANE &amp; HELICOPTER PILOTS</span></p>

      <div class="gauge-column">
        <svg class="gauge" style="top:21px" width="78" height="78" viewBox="0 0 78 78" role="img" aria-label="Airspeed indicator illustration">
          <circle cx="39" cy="39" r="37" fill="var(--gauge-face)" stroke="var(--accent)" stroke-width="3"/>
        </svg>
        <svg class="gauge" style="top:105px" width="78" height="78" viewBox="0 0 78 78" role="img" aria-label="Attitude indicator illustration">
          <circle cx="39" cy="39" r="37" fill="var(--gauge-face)" stroke="var(--accent)" stroke-width="3"/>
        </svg>
        <svg class="gauge" style="top:188px" width="78" height="78" viewBox="0 0 78 78" role="img" aria-label="Altimeter illustration">
          <circle cx="39" cy="39" r="37" fill="var(--gauge-face)" stroke="var(--accent)" stroke-width="3"/>
        </svg>
        <svg class="gauge" style="top:273px" width="78" height="78" viewBox="0 0 78 78" role="img" aria-label="Turn coordinator illustration">
          <circle cx="39" cy="39" r="37" fill="var(--gauge-face)" stroke="var(--accent)" stroke-width="3"/>
        </svg>
        <svg class="gauge" style="top:358px" width="78" height="78" viewBox="0 0 78 78" role="img" aria-label="Heading indicator illustration">
          <circle cx="39" cy="39" r="37" fill="var(--gauge-face)" stroke="var(--accent)" stroke-width="3"/>
        </svg>
      </div>

      <p class="front-tagline"><span class="tag-accent">PREPARE FOR YOUR IFR</span><br>RATING WITH CONFIDENCE</p>
      <div class="front-rule"></div>
      <p class="front-author">LIONEL J. QUARRICK</p>
    </section>
  </main>
</body>
</html>
```